Harvest Cobbler Bash

I am a Realtor and will be Mailing this Postcard to my best Clients Inviting them to Select the Pie they want for Thanksgiving and I will open my office for them to pick up. here's my thought on text:

THANK YOU HARVEST COBBLER BASH!
Tues Nov 25th 3 to 8PM

In Giving Thanks for Your Support and Referrals I want to Personally Invite You to My 1st Annual "Harvest Cobbler Bash". You have a choice of:
*Apple
*Pumpkin
*Pecan

Please let me know Your Choice by Mon Nov 17th. Please Feel Free to email me or Call Me with Your Pie Choice!

There will be Food and Drink Including My Award Winning Chili.

718 Larchmont Road
Gorham Me 04915
dana@danawhitmer.com
207.555.0148

Please Give it a Thanksgiving Look....I did not include a photo of a pie but open to it. PLEASE make the Paragraph "In Giving Thanks with the 3 Pie choices the Focal Point that Draws Your eyes to it.

```html
<!DOCTYPE html>
<html lang="en">
<head>
<meta charset="utf-8">
<title>Harvest Cobbler Bash Postcard</title>
<link rel="stylesheet" href="https://fonts.googleapis.com/css2?family=Libre+Baskerville:wght@400;700&family=Open+Sans:ital,wght@0,400;0,600;0,700;1,600&display=swap">
<style>
  :root {
    --ink: #2b1a12;
    --rust: #8a2a14;
    --orange: #f07f1e;
    --orange-deep: #e46a12;
    --paper: #ffffff;
    --line: #1b1b1b;
    --grey: #8d8d8d;
    --serif: "Libre Baskerville", "Times New Roman", serif;
    --sans: "Open Sans", Arial, sans-serif;
  }
  * { margin: 0; padding: 0; box-sizing: border-box; }
  html, body { width: 777px; height: 1200px; overflow: hidden; background: var(--paper); }
  .canvas { position: relative; width: 777px; height: 1200px; color: var(--ink); }

  /* Front */
  .front { position: absolute; left: 27px; top: 20px; width: 721px; height: 556px; overflow: hidden; }
  .front-photo { position: absolute; inset: 0;
    background:
      radial-gradient(ellipse 40% 26% at 70% 62%, #b86a2e 0%, #8a4a1e 50%, transparent 80%),
      radial-gradient(ellipse 30% 25% at 80% 8%, #d8621a 0%, transparent 70%),
      radial-gradient(ellipse 60% 40% at 55% 75%, #3a2a25 0%, #231714 70%),
      linear-gradient(135deg, #5a3a26 0%, #2a1a14 60%, #1e1410 100%); }
  .badge { position: absolute; left: 24px; top: 33px; width: 453px; height: 294px; }
  .badge svg { position: absolute; inset: 0; }
  .badge-text { position: absolute; inset: 0; text-align: center; color: var(--ink); }
  .badge-date { position: absolute; top: 26px; width: 100%; font-family: var(--serif); font-size: 23px; letter-spacing: 1px; }
  .badge-thanks { position: absolute; top: 74px; width: 100%; font-family: var(--sans); font-weight: 700; font-size: 42px; line-height: 56px; }
  .badge-title { position: absolute; top: 134px; width: 100%; font-family: var(--serif); font-size: 29px; line-height: 44px; color: var(--rust); letter-spacing: 1px; white-space: nowrap; }
  .badge-hours { position: absolute; top: 242px; width: 100%; font-family: var(--serif); font-size: 17px; }

  /* Back */
  .back { position: absolute; left: 24px; top: 605px; width: 721px; height: 559px; border: 2px solid var(--line); background: var(--paper); }
  .divider { position: absolute; left: 347px; top: 26px; width: 2px; height: 432px; background: var(--rust); }
  .invite { position: absolute; left: 17px; width: 320px; text-align: center; white-space: nowrap; }
  .brand { top: 20px; display: flex; align-items: center; justify-content: center; gap: 6px; height: 40px; }
  .brand-mark { width: 12px; height: 12px; background: var(--rust); }
  .brand-name { font-family: var(--sans); font-weight: 700; font-size: 17px; color: var(--rust); }
  .invite-thanks { top: 84px; font-family: var(--sans); font-weight: 700; font-size: 21px; line-height: 26px; }
  .invite-title { top: 110px; font-family: var(--serif); font-size: 18px; line-height: 23px; color: var(--rust); letter-spacing: 1px; }
  .invite-date { top: 159px; font-family: var(--serif); font-size: 16px; line-height: 20px; }
  .invite-place { top: 181px; font-family: var(--serif); font-size: 14px; line-height: 20px; }
  .focal { top: 212px; font-family: var(--sans); font-weight: 700; font-size: 13.5px; line-height: 20px; color: var(--rust); }
  .choices-lead { top: 282px; font-family: var(--sans); font-weight: 700; font-size: 15px; line-height: 20px; color: var(--rust); }
  .choices { top: 303px; font-family: var(--sans); font-weight: 700; font-size: 15px; line-height: 20px; }
  .rsvp { position: absolute; left: 20px; top: 334px; width: 240px; font-family: var(--sans); font-size: 13px; line-height: 19px; color: var(--ink); white-space: nowrap; }
  .rsvp b { font-weight: 700; }
  .extras { position: absolute; left: 20px; top: 413px; width: 160px; font-family: var(--sans); font-style: italic; font-weight: 600; font-size: 13.5px; line-height: 20px; color: var(--ink); }
  .pie-art { position: absolute; left: 186px; top: 398px; width: 168px; height: 82px; border-radius: 10px;
    background: radial-gradient(ellipse 60% 55% at 50% 60%, #a65a22 0%, #7e4018 60%, #d9b89a 85%, #f6eee4 100%); }

  .agent { position: absolute; left: 370px; top: 26px; }
  .agent-photo { width: 55px; height: 71px; border: 1px solid var(--ink); background: linear-gradient(180deg, #cfd6dc 0%, #8a95a0 100%); }
  .agent-info { margin-top: 14px; font-family: var(--sans); font-size: 12px; line-height: 16px; color: var(--ink); }
  .agent-name { font-style: italic; font-weight: 700; font-size: 13px; }
  .stamp { position: absolute; left: 581px; top: 40px; width: 98px; height: 113px; border: 1px solid var(--grey);
    font-family: var(--sans); font-weight: 600; font-size: 15px; line-height: 20px; color: var(--grey); padding: 26px 0 0 22px; }
</style>
</head>
<body>
<div class="canvas">

  <section class="front">
    <div class="front-photo" role="img" aria-label="Close-up photo of a slice of pumpkin pie with whipped cream on a dark plate, pumpkins behind"></div>
    <div class="badge">
      <svg viewBox="0 0 453 294" width="453" height="294" aria-hidden="true">
        <path d="M40 10 H413 Q421 30 443 34 V260 Q421 264 413 284 H40 Q32 264 10 260 V34 Q32 30 40 10 Z" fill="var(--ink)"/>
        <path d="M46 18 H407 Q415 36 435 40 V254 Q415 258 407 276 H46 Q38 258 18 254 V40 Q38 36 46 18 Z" fill="var(--orange)"/>
        <path d="M56 28 H397 Q405 44 423 48 V246 Q405 250 397 266 H56 Q48 250 30 246 V48 Q48 44 56 28 Z" fill="none" stroke="var(--orange-deep)" stroke-width="2"/>
        <circle cx="34" cy="147" r="7" fill="var(--ink)"/>
        <circle cx="419" cy="147" r="7" fill="var(--ink)"/>
        <line x1="112" y1="64" x2="341" y2="64" stroke="var(--ink)" stroke-width="1.5"/>
        <line x1="112" y1="230" x2="341" y2="230" stroke="var(--ink)" stroke-width="1.5"/>
      </svg>
      <div class="badge-text">
        <div class="badge-date">11.25.14</div>
        <div class="badge-thanks">THANK YOU!</div>
        <div class="badge-title">HARVEST COBBLER<br>BASH</div>
        <div class="badge-hours">3P.M. – 8P.M.</div>
      </div>
    </div>
  </section>

  <section class="back">
    <div class="invite brand"><span class="brand-mark"></span><span class="brand-name">Pine Harbor Realty Group</span></div>
    <div class="invite invite-thanks">THANK YOU!</div>
    <div class="invite invite-title">HARVEST COBBLER<br>BASH</div>
    <div class="invite invite-date">Tuesday November 25th 3P.M. – 8P.M.</div>
    <div class="invite invite-place">At My Office, 718 Larchmont Road</div>
    <p class="invite focal">In Giving Thanks for Your Support and<br>Referrals I want to Personally Invite You to<br>My 1st Annual "Harvest Cobbler Bash".</p>
    <p class="invite choices-lead">You have a choice of:</p>
    <p class="invite choices">Apple • Pumpkin • Pecan</p>

    <p class="rsvp">Please let me know Your Choice by<br><b>Monday November 17th.</b> Please Feel<br>Free to email me or Call Me with<br>Your Pie Choice!</p>
    <p class="extras">There will be Food and Drink Including My Award Winning Chili.</p>
    <div class="pie-art" role="img" aria-label="Slice of pumpkin pie topped with whipped cream"></div>

    <div class="divider"></div>

    <div class="agent">
      <div class="agent-photo" role="img" aria-label="Portrait photo of the agent"></div>
      <div class="agent-info">
        <div class="agent-name">Dana Whitmer</div>
        <div>718 Larchmont Road</div>
        <div>Gorham, ME 04915</div>
        <div>dana@danawhitmer.com</div>
        <div>207.555.0148</div>
      </div>
    </div>

    <div class="stamp">PLACE<br>STAMP<br>HERE</div>
  </section>

</div>
</body>
</html>
```